Song Cover Art. Song Tittle Lift The Floor

I would like a design for my songs. I'm a producer and i prouder EDM music such as Big Room House / Electro House music. Currently i have a new songs tittle name Lift The Floor and i need a cover art for my songs. I'm not sure what design i have in mind right now and i would like someone to create it for me. My DJ name is DJ Vex.
Reason: Hey, i will give sometimes for you guys to create the design for me. Please do zorvix edm cover art or brenlow - lift the floor.
Target Market(s)
Electronic Dance Music Lovers
Industry/Entity Type
House
Look and feel
Each slider illustrates characteristics of the customer's brand and the style your logo design should communicate.

```html
<!DOCTYPE html>
<html lang="en">
<head>
<meta charset="utf-8">
<title>Lift The Floor — DJ Vex</title>
<link rel="stylesheet" href="https://fonts.googleapis.com/css2?family=Exo+2:ital,wght@1,700;1,800&display=swap">
<style>
  :root {
    --bg-deep: #1a0624;
    --bg-mid: #4a1468;
    --bg-glow: #9b3fc8;
    --magenta: #e04cf0;
    --pink-light: #f6b8ff;
    --violet: #6a36b8;
    --teal-edge: #3fd8e0;
    --white: #ffffff;
  }
  * { margin: 0; padding: 0; box-sizing: border-box; }
  html, body {
    width: 1200px;
    height: 1200px;
    overflow: hidden;
    background: var(--bg-deep);
  }
  .cover {
    position: relative;
    width: 1200px;
    height: 1200px;
    overflow: hidden;
    font-family: "Exo 2", sans-serif;
  }
  .cover-photo {
    position: absolute;
    inset: 0;
    background:
      radial-gradient(circle at 30% 45%, rgba(224, 76, 240, 0.55), transparent 45%),
      radial-gradient(circle at 75% 30%, rgba(155, 63, 200, 0.45), transparent 40%),
      radial-gradient(circle at 40% 90%, rgba(120, 60, 180, 0.5), transparent 45%),
      linear-gradient(160deg, var(--bg-deep) 0%, var(--bg-mid) 55%, var(--bg-deep) 100%);
  }
  .title {
    position: absolute;
    inset: 0;
    font-size: inherit;
    font-weight: inherit;
  }
  .title-line {
    position: absolute;
    display: block;
    font-size: 310px;
    font-weight: 800;
    font-style: italic;
    line-height: 1;
    letter-spacing: -6px;
    text-transform: uppercase;
    white-space: nowrap;
    background: linear-gradient(180deg, var(--pink-light) 0%, var(--magenta) 45%, var(--violet) 100%);
    -webkit-background-clip: text;
    background-clip: text;
    color: transparent;
    filter:
      drop-shadow(0 0 1px var(--teal-edge))
      drop-shadow(0 0 1px var(--teal-edge))
      drop-shadow(0 0 14px var(--magenta));
  }
  .title-line--one { left: 50px; top: 0; }
  .title-line--two {
    left: 150px; top: 224px;
    background: linear-gradient(180deg, var(--white) 0%, var(--pink-light) 50%, var(--magenta) 100%);
    -webkit-background-clip: text;
    background-clip: text;
  }
  .title-line--three { left: 205px; top: 448px; }
  .artist {
    position: absolute;
    right: 44px;
    top: 1036px;
    font-size: 132px;
    font-weight: 700;
    font-style: italic;
    line-height: 1;
    text-transform: uppercase;
    color: var(--white);
    filter: drop-shadow(0 0 10px var(--magenta));
  }
</style>
</head>
<body>
  <main class="cover">
    <div class="cover-photo" role="img" aria-label="Macro photo of dandelion seed fibres covered in glistening water droplets, lit in violet and magenta with soft bokeh"></div>
    <h1 class="title">
      <span class="title-line title-line--one">Lift</span>
      <span class="title-line title-line--two">The</span>
      <span class="title-line title-line--three">Floor</span>
    </h1>
    <p class="artist">DJ Vex</p>
  </main>
</body>
</html>
```